Dalvor Inc Business Card

Looking to get an updated business card for a Contract Machining company (www.dalvorinc-example.com) - looking for a clean design the portrays the technical nature of the business - colors can follow the website design and be in any combination that makes sense (red black, white, metallic or silver) - logos attached for use also. Would like space for: Name, title, business phone (555 214-3098), cell phone , website (www.dalvorinc-example.com) - possibly QR code could be integrated for website (designer choice), business address - 418 Birchfield Lane, Millbrook Falls, MI 49990 (cards will be for 4 employees, I will either need to modify a template or I can provide individual information)
Target Market(s)
Aerospace, defense and medical device manufacturing companies that need machining
Industry/Entity Type
Machining for aerospace, defense, medical
Contact Information for Business Card
Name, Title, Business Phone, Cell Phone, email, business website and business address

```html
<!DOCTYPE html>
<html lang="en">
<head>
<meta charset="utf-8">
<title>Dalvor Inc Business Card</title>
<link href="https://fonts.googleapis.com/css2?family=Montserrat:wght@400;500;800&display=swap" rel="stylesheet">
<style>
  :root{
    --red:#c1151c;
    --ink:#555a60;
    --paper:#ffffff;
    --black:#1f1f21;
    --stage:#2e2f31;
  }
  *{margin:0;padding:0;box-sizing:border-box}
  html,body{width:1200px;height:900px;overflow:hidden;background:var(--stage);font-family:'Montserrat',sans-serif}
  .canvas{position:relative;width:1200px;height:900px}
  .card{position:absolute;top:302px;width:520px;height:297px;overflow:hidden}
  .card--front{left:50px;background:var(--paper);border-bottom:4px solid var(--red)}
  .card--back{left:630px;background:var(--black);border:3px solid var(--red)}

  .tab{position:absolute;left:22px;top:0;width:118px;height:36px;background:var(--red)}
  .brand__mark{position:absolute;left:30px;top:12px;width:70px;height:70px;border-radius:50%;background:var(--red);border:4px solid var(--paper);box-shadow:0 0 0 2px var(--red)}
  .brand__name{position:absolute;left:30px;top:94px;font-weight:800;font-size:26px;line-height:32px;color:var(--red);letter-spacing:0.5px;white-space:nowrap}

  .person{position:absolute;right:34px;top:98px;text-align:right}
  .person__name{font-weight:800;font-size:20px;line-height:24px;color:var(--red);letter-spacing:0.5px;white-space:nowrap}
  .person__title{font-weight:500;font-size:12px;line-height:16px;color:var(--ink);letter-spacing:1.5px}
  .divider{position:absolute;left:28px;right:28px;top:148px;height:2px;background:var(--red)}

  .contacts{position:absolute;left:28px;top:164px;list-style:none}
  .contacts li{display:flex;align-items:center;gap:8px;font-size:13px;color:var(--ink);line-height:24px;white-space:nowrap}
  .contacts svg{width:11px;height:11px;fill:none;stroke:var(--red);stroke-width:2}
  .address{position:absolute;right:34px;top:190px;text-align:right;font-size:15px;color:var(--ink);line-height:24px;white-space:nowrap}

  .back-brand{position:absolute;left:0;right:0;top:48px;display:flex;flex-direction:column;align-items:center;gap:18px}
  .back-brand__mark{width:140px;height:140px;border-radius:50%;background:var(--red)}
  .back-brand__name{font-weight:800;font-size:30px;color:var(--red);letter-spacing:0.5px}
</style>
</head>
<body>
<main class="canvas">
  <section class="card card--front" aria-label="Business card front">
    <div class="tab"></div>
    <div class="brand__mark"></div>
    <div class="brand__name">DALVOR INC.</div>
    <div class="person">
      <div class="person__name">JORDAN AVERY</div>
      <div class="person__title">DIRECTOR</div>
    </div>
    <div class="divider"></div>
    <ul class="contacts">
      <li><svg viewBox="0 0 12 12"><path d="M2 1l2 0 1 3-1.5 1a6 6 0 0 0 3.5 3.5L8 7l3 1v2a1 1 0 0 1-1 1A9 9 0 0 1 1 2a1 1 0 0 1 1-1z"/></svg>555 214-3098</li>
      <li><svg viewBox="0 0 12 12"><rect x="3" y="1" width="6" height="10" rx="1"/></svg>555-867-4021</li>
      <li><svg viewBox="0 0 12 12"><rect x="1" y="2.5" width="10" height="7"/><path d="M1 2.5l5 4 5-4"/></svg>info@dalvorinc-example.com</li>
      <li><svg viewBox="0 0 12 12"><circle cx="6" cy="6" r="5"/><path d="M1 6h10M6 1c-3 3-3 7 0 10M6 1c3 3 3 7 0 10"/></svg>www.dalvorinc-example.com</li>
    </ul>
    <div class="address">418 Birchfield Lane,<br>Millbrook Falls, MI 49990</div>
  </section>

  <section class="card card--back" aria-label="Business card back">
    <div class="back-brand">
      <div class="back-brand__mark"></div>
      <div class="back-brand__name">DALVOR INC.</div>
    </div>
  </section>
</main>
</body>
</html>
```